Liposomal Powders and Excipient Free Manufacturing

I’m seeking a talented designer to refine and elevate a PowerPoint presentation aimed at healthcare professionals. The goal is to ensure the slides are clean, professional, and visually aligned with a scientific audience while remaining engaging and easy to follow.
What I Need:
- Optimisation of slide layouts for clarity and visual impact.
- Creation of a cohesive master template that reflects the brand’s professional and scientific tone.
- Use of brand guidelines (including fonts, colours, and logos) to maintain consistency.
- Strategic incorporation of relevant images, graphics, or icons to make the content more engaging and support the messaging.
- A final design that feels polished, modern, and ready for professional delivery.
What I’ll Provide:
- Current PowerPoint presentation.
- Brand guidelines with fonts, colours, and logo files.

Ideal Designer:
- Experienced in professional or corporate PowerPoint design.
- Comfortable working with scientific or healthcare-related content.
- Able to deliver a clean, visually cohesive presentation that feels on-brand and audience-appropriate.

```html
<!DOCTYPE html>
<html lang="en">
<head>
<meta charset="utf-8">
<title>Smarter Delivery – Slide Overview</title>
<link href="https://fonts.googleapis.com/css2?family=Lato:wght@400;700;900&display=swap" rel="stylesheet">
<style>
:root{
  --canvas:#eaf6f8;
  --teal:#149aae;
  --teal-light:#5cc3cf;
  --teal-pale:#d8f0f3;
  --ink:#2b2b2b;
  --ink-soft:#444;
  --paper:#ffffff;
}
*{margin:0;padding:0;box-sizing:border-box}
html,body{width:1058px;height:1200px;overflow:hidden;background:var(--canvas);font-family:'Lato',sans-serif;color:var(--ink)}
.slide{position:absolute;width:424px;height:238px;background:var(--paper);overflow:hidden;box-shadow:0 2px 8px rgba(20,80,90,.12)}
.slide.band::before{content:"";position:absolute;left:0;top:0;width:24px;height:100%;background:var(--teal)}
.t{position:absolute;line-height:1;white-space:nowrap}
.ring{position:absolute;left:6px;top:10px;width:32px;height:32px;border-radius:50%;border:1.5px solid var(--teal-light);background:var(--paper)}
.slide-title{position:absolute;left:20px;top:21px;font-size:11px;font-weight:700;color:var(--ink);letter-spacing:.1px}
.slide-title.wide{left:21px}
.brand{position:absolute;right:18px;top:22px;display:flex;align-items:center;gap:3px;font-size:6px;font-weight:400;color:var(--ink);letter-spacing:.2px}
.brand i{width:9px;height:9px;border-radius:50%;border:1px solid var(--teal)}
.foot-date{position:absolute;left:54px;top:226px;font-size:5.2px;font-weight:700}
.foot-num{position:absolute;right:22px;top:226px;font-size:5.2px;font-weight:700}
.media{position:absolute}
.teal{color:var(--teal)}
.tick{display:inline-block;width:6px;height:6px;border-radius:50%;background:var(--teal-light);margin-right:5px;vertical-align:middle;position:relative}
.tick::after{content:"";position:absolute;left:1.6px;top:1.2px;width:2.4px;height:1.4px;border-left:1px solid #fff;border-bottom:1px solid #fff;transform:rotate(-45deg)}
.wave{position:absolute;inset:0;background:linear-gradient(160deg,#fff 30%,#f1f1f1 55%,#fff 70%,#ececec 90%)}
.circle-cap{position:absolute;font-size:6.2px;text-align:center;line-height:1.4;width:90px;margin-left:-45px}
.benefit{position:absolute;width:62px;height:62px;margin:-31px 0 0 -31px;border-radius:50%;background:var(--teal-pale);display:flex;align-items:center;justify-content:center}
.benefit span{width:46px;height:46px;border-radius:50%;background:var(--teal);display:flex;align-items:center;justify-content:center}
.photo-round{position:absolute;width:62px;height:62px;margin:-31px 0 0 -31px;border-radius:50%}
.contact{position:absolute;font-size:7.5px}
.contact b{display:block;font-weight:400;font-size:8px;color:var(--ink);margin-bottom:4px}
.contact span{color:var(--ink-soft)}
.pin{position:absolute;width:18px;height:18px;border-radius:50%;background:var(--teal);display:flex;align-items:center;justify-content:center}
</style>
</head>
<body>

<!-- Slide 01: cover -->
<section class="slide" style="left:68px;top:65px">
  <div class="media" role="img" aria-label="Dotted teal circular decoration" style="left:0;top:0;width:210px;height:238px;background:radial-gradient(circle at 90px 120px,transparent 60px,rgba(92,195,207,.18) 62px,rgba(20,154,174,.10) 110px,transparent 125px)"></div>
  <div class="media" role="img" aria-label="Photo of a smiling woman with arms outstretched by a lake" style="left:200px;top:0;width:224px;height:238px;background:linear-gradient(90deg,#fff 0%,rgba(255,255,255,0) 35%),linear-gradient(180deg,#e9eef2 0%,#c9d4da 45%,#8fa2ab 70%,#7b8b5e 100%)"></div>
  <div class="t" style="left:80px;top:76px;font-size:10px;display:flex;align-items:center;gap:3px"><i style="width:12px;height:12px;border-radius:50%;border:1px solid var(--teal);display:inline-block"></i>NUTRAVELA</div>
  <div class="t" style="left:66px;top:104px;font-size:17.5px;font-weight:700;letter-spacing:.2px">SMARTER DELIVERY</div>
  <div class="t" style="left:66px;top:129px;font-size:7.8px">The Clinical Edge of Novel Liposomal Powders</div>
  <div class="t" style="left:66px;top:144px;font-size:7.8px">&amp; Excipient-Free Manufacturing</div>
  <div class="t" style="left:66px;top:161px;font-size:7.8px">Verdant Expo 2025 | <span class="teal">Presented by Dr Elias Warren</span></div>
</section>

<!-- Slide 02: contents -->
<section class="slide band" style="left:562px;top:65px">
  <div class="ring"></div>
  <div class="slide-title">TABLE OF CONTENT</div>
  <div class="brand"><i></i>NUTRAVELA</div>
  <div class="t teal" style="left:53px;top:45px;font-size:10px;font-weight:700">Part I – Liposomal Innovation &amp; Super-Dried Powders</div>
  <div class="t" style="left:53px;top:65px;font-size:7.2px"><span class="tick"></span>Why Delivery Technology Matters</div>
  <div class="t" style="left:53px;top:81px;font-size:7.2px"><span class="tick"></span>Liposome Basics&nbsp; Powders&nbsp; Stability</div>
  <div class="t" style="left:53px;top:97px;font-size:7.2px"><span class="tick"></span>Clinical Evidence (Vitamin B12, Vitamin C, CoQ10, Iron, PEA, Glutathione, Resveratrol)</div>
  <div class="t" style="left:53px;top:113px;font-size:7.2px"><span class="tick"></span>Manufacturing Essentials: Spray &amp; Lyophilization Drying, Stability Considerations</div>
  <div class="t teal" style="left:53px;top:131px;font-size:10px;font-weight:700">Part II - Clean Manufacturing</div>
  <div class="t" style="left:53px;top:149px;font-size:7.2px"><span class="tick"></span>Excipient-Free Manufacturing: Why It Matters</div>
  <div class="t" style="left:53px;top:165px;font-size:7.2px"><span class="tick"></span>Case Studies &amp; Challenges</div>
  <div class="t" style="left:53px;top:180px;font-size:7.2px"><span class="tick"></span>Key Takeaways</div>
  <div class="t" style="left:53px;top:196px;font-size:7.2px"><span class="tick"></span>Q&amp;A</div>
  <div class="foot-date">24 Sept 2025</div><div class="foot-num">02</div>
</section>

<!-- Slide 03: section divider -->
<section class="slide band" style="left:68px;top:352px">
  <div class="wave"></div>
  <div class="ring"></div>
  <div class="slide-title">LIPOSOMAL INNOVATION</div>
  <div class="brand"><i></i>NUTRAVELA</div>
  <div class="t teal" style="left:24px;right:0;text-align:center;top:80px;font-size:19px;font-weight:700;margin-left:-4px">PART I</div>
  <div class="t" style="left:24px;right:0;text-align:center;top:109px;font-size:20.5px;font-weight:700;color:#333">LIPOSOMAL INNOVATION &amp;</div>
  <div class="t" style="left:24px;right:0;text-align:center;top:136px;font-size:18px;font-weight:700;color:#333">SUPER-DRIED POWDERS</div>
  <div class="foot-date">24 Sept 2025</div><div class="foot-num">03</div>
</section>

<!-- Slide 04: why delivery matters -->
<section class="slide band" style="left:562px;top:352px">
  <div class="ring"></div>
  <div class="slide-title wide">WHY DELIVERY TECHNOLOGY MATTERS?</div>
  <div class="brand"><i></i>NUTRAVELA</div>
  <div class="media" role="img" aria-label="Photo of a scientist working in a laboratory" style="left:52px;top:53px;width:154px;height:154px;border-radius:50%;background:linear-gradient(135deg,#eef3f6,#c7d5de 60%,#9fb3c0)"></div>
  <svg class="media" style="left:236px;top:49px" width="10" height="10" viewBox="0 0 10 10"><path d="M5 1 L9 9 H1 Z" fill="#2b2b2b"/><circle cx="5" cy="6.5" r="1" fill="#fff"/></svg>
  <div class="t" style="left:236px;top:65px;font-size:7.5px">CHALLENGE</div>
  <div class="t" style="left:236px;top:78px;font-size:6px;line-height:1.9;white-space:normal;width:160px">Poor solubility, instability, first-pass metabolism, and GI irritation often lead to low or inconsistent bioavailability.</div>
  <svg class="media" style="left:236px;top:121px" width="10" height="11" viewBox="0 0 10 11"><circle cx="5" cy="4" r="3" fill="var(--teal)"/><rect x="4" y="7" width="2" height="3" fill="var(--teal)"/></svg>
  <div class="t" style="left:236px;top:138px;font-size:7.5px">SOLUTION</div>
  <div class="t" style="left:236px;top:151px;font-size:6px;line-height:1.9;white-space:normal;width:160px">Liposomal and solid-lipid delivery systems protect active ingredients, improve dissolution, and enhance absorption.</div>
  <div class="t" style="left:236px;top:190px;font-size:8px;font-weight:700">Better delivery = Better Clinical Outcomes</div>
  <div class="foot-date">24 Sept 2025</div><div class="foot-num">04</div>
</section>

<!-- Slide 05: what is a liposome -->
<section class="slide band" style="left:68px;top:633px">
  <div class="ring"></div>
  <div class="slide-title wide">WHAT IS A LIPOSOME?</div>
  <div class="brand"><i></i>NUTRAVELA</div>
  <div class="media" role="img" aria-label="Cross-section illustration of a liposome with labelled phospholipid layers" style="left:53px;top:60px;width:140px;height:150px;border-radius:50%;background:radial-gradient(circle at 75px 75px,#2f8f8a 0,#4fb1a6 30px,#bfe3e8 46px,#eaf6f8 60px,transparent 72px)"></div>
  <div class="t" style="left:223px;top:56px;font-size:8.7px;line-height:1.72;white-space:normal;width:185px">Liposomes are microscopic spheres made of natural phospholipids that mimic human cell membranes, allowing nutrients to be absorbed more efficiently.</div>
  <div class="media" role="img" aria-label="Photo of a family blowing bubbles on a sunny lawn" style="left:223px;top:140px;width:179px;height:72px;border-radius:36px;background:linear-gradient(180deg,#f3d98a,#c9a85a 45%,#7f9a3e 100%)"></div>
  <div class="foot-date">24 Sept 2025</div><div class="foot-num">05</div>
</section>

<!-- Slide 06: liquids to powders -->
<section class="slide band" style="left:562px;top:633px">
  <div class="ring"></div>
  <div class="slide-title wide">FROM LIQUIDS TO "<span class="teal">SUPER-DRIED</span>" POWDERS</div>
  <div class="brand"><i></i>NUTRAVELA</div>
  <div class="t" style="left:53px;top:56px;font-size:8px;line-height:1.65;white-space:normal;width:340px"><span class="tick"></span>Liquid liposomes are traditional but can pose challenges for stability, dosing, and consumer convenience.</div>
  <div class="t" style="left:53px;top:86px;font-size:8px"><span class="tick"></span>Converting liposomes to powders via spray-drying or lyophilization provides:</div>
  <div class="benefit" style="left:85px;top:143px"><span><svg width="20" height="20" viewBox="0 0 20 20" fill="#fff"><rect x="4" y="3" width="12" height="14" rx="1"/><rect x="6" y="6" width="8" height="1.5" fill="var(--teal)"/><rect x="6" y="9" width="8" height="1.5" fill="var(--teal)"/><rect x="6" y="12" width="5" height="1.5" fill="var(--teal)"/></svg></span></div>
  <div class="benefit" style="left:179px;top:143px"><span><svg width="20" height="20" viewBox="0 0 20 20" fill="#fff"><rect x="8" y="2" width="4" height="9"/><circle cx="10" cy="14" r="4"/></svg></span></div>
  <div class="benefit" style="left:272px;top:143px"><span><svg width="20" height="20" viewBox="0 0 20 20" fill="#fff"><path d="M7 3 C4 8 3 10 3 12 a4 4 0 0 0 8 0 C11 10 10 8 7 3Z"/><path d="M14 7 C12 10 11 12 11 13 a3 3 0 0 0 6 0 C17 12 16 10 14 7Z"/></svg></span></div>
  <div class="benefit" style="left:366px;top:143px"><span><svg width="20" height="20" viewBox="0 0 20 20"><circle cx="10" cy="10" r="7" fill="none" stroke="#fff" stroke-width="1.8"/><path d="M10 6 V10 L13 12" stroke="#fff" stroke-width="1.8" fill="none"/></svg></span></div>
  <div class="circle-cap" style="left:85px;top:176px">Higher active<br>load</div>
  <div class="circle-cap" style="left:179px;top:175px">Improved handling &amp;<br>formulation flexibility</div>
  <div class="circle-cap" style="left:272px;top:176px">Significantly reduced<br>oxidation compared to<br>liquids</div>
  <div class="circle-cap" style="left:366px;top:175px">Longer<br>shelf-life</div>
  <div class="foot-date">24 Sept 2025</div><div class="foot-num">06</div>
</section>

<!-- Slide 07: stability levers -->
<section class="slide band" style="left:68px;top:912px">
  <div class="ring"></div>
  <div class="slide-title wide">STABILITY LEVERS IN DRIED LIPOSOMES</div>
  <div class="brand"><i></i>NUTRAVELA</div>
  <div class="photo-round" role="img" aria-label="Photo of a worker loading cartons into a truck" style="left:85px;top:89px;background:linear-gradient(135deg,#6b5a4a,#c49a6c 60%,#e8d3b0)"></div>
  <div class="photo-round" role="img" aria-label="Photo of fresh berries in a punnet" style="left:228px;top:89px;background:radial-gradient(circle,#c0243a,#5a1f3a 70%,#3a3f6a)"></div>
  <div class="photo-round" role="img" aria-label="Photo of plastic water bottles" style="left:372px;top:89px;background:linear-gradient(180deg,#e9eef2,#b9cdd8 55%,#8a6a4a)"></div>
  <div class="photo-round" role="img" aria-label="Photo of a honey jar with red berries and blossom" style="left:157px;top:160px;background:linear-gradient(160deg,#5d7f96,#9fb8c8 40%,#b2632a 75%,#2f4b60)"></div>
  <div class="photo-round" role="img" aria-label="Photo of a seedling growing through cracked ground" style="left:300px;top:160px;background:linear-gradient(180deg,#dce6ea,#8fa4ab 50%,#4a5a60)"></div>
  <div class="circle-cap" style="left:85px;top:125px">Matrix (carriers, glass<br>transition)</div>
  <div class="circle-cap" style="left:228px;top:125px">Antioxidants/<br>chelators</div>
  <div class="circle-cap" style="left:372px;top:125px">Packaging &amp; water<br>activity</div>
  <div class="circle-cap" style="left:157px;top:196px">Residual moisture</div>
  <div class="circle-cap" style="left:300px;top:196px">Particle size &amp;<br>agglomeration</div>
  <div class="foot-date">24 Sept 2025</div><div class="foot-num">07</div>
</section>

<!-- Slide 08: contact -->
<section class="slide band" style="left:562px;top:912px">
  <div class="wave"></div>
  <div class="ring"></div>
  <div class="slide-title wide">CONTACT US</div>
  <div class="t" style="left:24px;right:0;top:56px;display:flex;justify-content:center;align-items:center;gap:6px;font-size:16px;color:#444"><i style="width:22px;height:22px;border-radius:50%;border:1.5px solid var(--teal);display:inline-block"></i>NUTRAVELA</div>
  <div class="t" style="left:24px;right:0;top:101px;text-align:center;font-size:8.2px;line-height:1.6;white-space:normal;padding:0 20px">We’re here to answer your questions and provide the support you need. Whether it’s about our services, partnerships, or general inquiries, our team is ready to assist you.</div>
  <div class="pin" style="left:55px;top:140px"><svg width="9" height="11" viewBox="0 0 9 11"><path d="M4.5 0.5a3.8 3.8 0 0 1 3.8 3.8C8.3 7 4.5 10.5 4.5 10.5S0.7 7 0.7 4.3A3.8 3.8 0 0 1 4.5 0.5Z" fill="#fff"/><circle cx="4.5" cy="4.3" r="1.4" fill="var(--teal)"/></svg></div>
  <div class="contact" style="left:80px;top:138px"><b>Location</b><span>Nutravela, US</span></div>
  <div class="pin" style="left:172px;top:140px"><svg width="10" height="10" viewBox="0 0 10 10"><path d="M2 1 L4 1 L5 3.5 L3.8 4.5 C4.4 5.8 5.2 6.6 6.5 7.2 L7.5 6 L10 7 L10 9 C5 9.5 0.5 5 1 1Z" fill="#fff"/></svg></div>
  <div class="contact" style="left:198px;top:139px"><b>Call Us</b><span>+1 555 010 2040</span></div>
  <div class="pin" style="left:283px;top:140px"><svg width="10" height="8" viewBox="0 0 10 8"><rect x="0.5" y="0.5" width="9" height="7" rx="1" fill="#fff"/><path d="M1 1 L5 4.5 L9 1" stroke="var(--teal)" fill="none" stroke-width="1"/></svg></div>
  <div class="contact" style="left:308px;top:139px"><b>Mail Us</b><span>info@nutravela.com</span></div>
  <div class="t teal" style="left:24px;right:0;top:179px;text-align:center;font-size:15px;font-weight:700">THANK YOU</div>
  <div class="foot-date">24 Sept 2025</div><div class="foot-num">08</div>
</section>

</body>
</html>
```